Healthy Supplement featuring Moringa products

Need 3 business card options for our reps to order from Cardloom. Our reps will be ordering from Cardloom once we upload them. Attached is our current designs to show what info needs to be on the cards. Our website is www.tkvitality.com
The business cards will be a template for our reps to order from. Most of our reps are Asian & Hispanic. Please look at our website so you can see who we are to get the look and feel what we need.
Target Market(s)
Adults 30 on up. Health oriented people.
Industry/Entity Type
Health And Wellness
Contact Information for Business Card
Name
Title
Phone
Logo
www.tkvitality.com/my/username
Font styles to use
Requirements
Must have
- Please match our website look and colors. A moringa leaf is nice, but am open to something different.
Nice to have
- Healthy looking and warm, not super cold or too modern.
Should not have
- No harsh colors please.

```html
<!DOCTYPE html>
<html lang="en">
<head>
<meta charset="UTF-8">
<title>TK Vitality Business Card</title>
<link href="https://fonts.googleapis.com/css2?family=Cinzel:wght@500&family=Work+Sans:wght@400;500&display=swap" rel="stylesheet">
<style>
  :root {
    --leaf-green: #6aa843;
    --fresh-green: #8cc63f;
    --ink: #3a3a3a;
    --paper: #ffffff;
    --backdrop: #2b2b2b;
  }
  * { margin: 0; padding: 0; box-sizing: border-box; }
  html, body { width: 1200px; height: 900px; overflow: hidden; }
  body {
    background: var(--backdrop);
    font-family: "Work Sans", Arial, sans-serif;
    position: relative;
  }
  .card {
    position: absolute;
    left: 260px;
    width: 680px;
    height: 389px;
    border-radius: 26px;
    overflow: hidden;
  }
  .card--front { top: 46px; background: var(--paper); }
  .card--back { top: 466px; background: var(--leaf-green); }

  .rep-name {
    position: absolute;
    left: 44px; top: 52px;
    font-family: "Cinzel", Georgia, serif;
    font-weight: 500;
    font-size: 27px;
    color: var(--fresh-green);
    letter-spacing: 0.5px;
  }
  .divider {
    position: absolute;
    left: 218px; top: 112px;
    width: 420px; height: 1.5px;
    background: var(--fresh-green);
  }
  .rep-details {
    position: absolute;
    left: 44px; top: 96px;
    color: var(--ink);
    font-size: 16px;
    line-height: 24px;
    list-style: none;
  }
  .rep-details .title { margin-bottom: 4px; }
  .rep-details .address { margin-bottom: 8px; }
  .contact { display: flex; align-items: center; gap: 8px; }
  .contact svg { width: 12px; height: 12px; fill: var(--fresh-green); flex: none; }
  .contact .accent { color: var(--fresh-green); }

  .brand {
    position: absolute;
    display: flex;
    align-items: center;
    font-family: "Cinzel", Georgia, serif;
    font-weight: 500;
    letter-spacing: 3px;
  }
  .brand--front {
    right: 44px; top: 58px;
    font-size: 30px;
    color: var(--leaf-green);
    gap: 12px;
  }
  .brand--front .brand-dot {
    width: 22px; height: 22px; border-radius: 50%;
    background: var(--fresh-green);
  }
  .brand--back {
    left: 0; right: 0; top: 0; bottom: 0;
    justify-content: center;
    gap: 20px;
    font-size: 54px;
    color: var(--paper);
  }
  .brand--back .brand-dot {
    width: 40px; height: 40px; border-radius: 50%;
    background: var(--paper);
  }
</style>
</head>
<body>

<section class="card card--front">
  <h1 class="rep-name">Daniel Reyes</h1>
  <div class="divider"></div>
  <div class="brand brand--front"><span class="brand-dot"></span>TK Vitality</div>
  <ul class="rep-details">
    <li class="title">Director</li>
    <li>418 Willow Ave. STE B</li>
    <li class="address">Fairview, CA 92410</li>
    <li class="contact">
      <svg viewBox="0 0 24 24"><path d="M6.6 10.8a15 15 0 0 0 6.6 6.6l2.2-2.2c.3-.3.7-.4 1-.2 1.1.4 2.3.6 3.6.6.6 0 1 .4 1 1V20c0 .6-.4 1-1 1A17 17 0 0 1 3 4c0-.6.4-1 1-1h3.5c.6 0 1 .4 1 1 0 1.3.2 2.5.6 3.6.1.3 0 .7-.2 1z"/></svg>
      555 214-3360
    </li>
    <li class="contact">
      <svg viewBox="0 0 24 24"><circle cx="12" cy="6" r="5"/><circle cx="6" cy="15" r="5"/><circle cx="18" cy="15" r="5"/></svg>
      555 218-7741
    </li>
    <li class="contact">
      <svg viewBox="0 0 24 24"><path d="M2 5h20v14H2zm2 2v.5l8 5 8-5V7zm0 2.8V17h16V9.8l-8 5z"/></svg>
      info@tkvitality.com
    </li>
    <li class="contact">
      <svg viewBox="0 0 24 24"><circle cx="12" cy="12" r="10"/></svg>
      <span>www.<span class="accent">tkvitality</span>.com</span>
    </li>
  </ul>
</section>

<section class="card card--back">
  <div class="brand brand--back"><span class="brand-dot"></span>TK Vitality</div>
</section>

</body>
</html>
```